Family owned plumbing contractor needs eye catching business card design

Business cards that are unique, eye catching, and provide customers with general company information, such as name, address, phone number, website, employee name/title, cell phone #, & email address. We are transitioning to a new logo that utilizes a more retro feel, so we are interested in seeing some cool old school designs in the mix. We are liking the dark background on some of the samples on this website. If that is workable with our artwork, we would like to see that incorporated into the design.
Contact Information for Business Card
Copperline Pipeworks, Inc.
www.copperlinepipeworks.example
(555) 630-2918 phone
Nevada License #64205
California License #5870413
Glen Harwick, President
(555) 418-9063 cell
glen@copperlinepipeworks.example
Residential * Commercial * Service
Requirements
Must have
- The business card details listed above & logo provided.
Nice to have
- I made some notes about color options in the description.

```html
<!DOCTYPE html>
<html lang="en">
<head>
<meta charset="utf-8">
<title>Copperline Pipeworks, Inc. – Business Card</title>
<link rel="stylesheet" href="https://fonts.googleapis.com/css2?family=Roboto:wght@400;500;700&display=swap">
<style>
  :root {
    --slate-blue: #4f7592;
    --slate-blue-deep: #456a86;
    --paper: #ededed;
    --ink: #4a4d52;
    --name-blue: #4e7895;
    --mint: #6fd1b9;
    --backdrop: #d9dbdd;
    --white: #ffffff;
  }
  * { box-sizing: border-box; margin: 0; padding: 0; }
  html, body { width: 1200px; height: 782px; overflow: hidden; }
  body {
    background: var(--backdrop);
    font-family: "Roboto", Arial, sans-serif;
    position: relative;
  }
  .card {
    position: absolute;
    width: 560px;
    height: 320px;
    box-shadow: 0 6px 18px rgba(0,0,0,0.18);
    overflow: hidden;
  }
  /* Front */
  .card-front { left: 60px; top: 70px; background: var(--paper); }
  .front-band {
    position: absolute; left: 0; top: 0; width: 100%; height: 96px;
    background: linear-gradient(180deg, var(--slate-blue) 0%, var(--slate-blue-deep) 100%);
  }
  .holder { position: absolute; left: 34px; bottom: 58px; }
  .holder-name {
    font-weight: 700; font-size: 30px; letter-spacing: 0.5px;
    color: var(--name-blue); text-transform: uppercase; line-height: 1;
  }
  .holder-title {
    font-weight: 500; font-size: 18px; letter-spacing: 0.5px;
    color: var(--mint); text-transform: uppercase; margin-top: 2px;
  }
  .details {
    position: absolute; left: 300px; top: 118px;
    font-size: 13.5px; color: var(--ink); line-height: 1.3;
  }
  .company-block { margin-bottom: 16px; }
  .contact-row .label { color: var(--name-blue); font-weight: 700; display: inline-block; width: 18px; }
  /* Back */
  .card-back {
    left: 580px; top: 392px;
    background: linear-gradient(160deg, var(--slate-blue) 0%, var(--slate-blue-deep) 100%);
  }
  .back-texture { position: absolute; inset: 0; }
  .brand {
    position: absolute; left: 0; right: 0; top: 118px;
    display: flex; align-items: center; justify-content: center; gap: 12px;
  }
  .brand-dot { width: 16px; height: 16px; border-radius: 50%; background: var(--mint); }
  .brand-name { font-weight: 700; font-size: 28px; color: var(--white); letter-spacing: 0.5px; }
  .services {
    position: absolute; right: 40px; bottom: 44px;
    font-size: 14px; color: var(--white); letter-spacing: 1px; text-transform: uppercase;
  }
  .services .sep { margin: 0 6px; }
</style>
</head>
<body>
  <section class="card card-front">
    <div class="front-band" role="img" aria-label="Slate blue band with white cracked marble texture"></div>
    <div class="holder">
      <div class="holder-name">Glen Harwick</div>
      <div class="holder-title">President</div>
    </div>
    <div class="details">
      <div class="company-block">
        <div>Copperline Pipeworks, Inc</div>
        <div>California License #5870413</div>
        <div>Nevada License #64205</div>
      </div>
      <div class="contact-row"><span class="label">P:</span> (555) 630-2918</div>
      <div class="contact-row"><span class="label">M:</span> (555) 418-9063</div>
      <div class="contact-row"><span class="label">E:</span>glen@copperlinepipeworks.example</div>
      <div class="contact-row"><span class="label">W:</span> www.copperlinepipeworks.example</div>
    </div>
  </section>

  <section class="card card-back">
    <div class="back-texture" role="img" aria-label="Slate blue cracked marble texture covering the card"></div>
    <div class="brand">
      <span class="brand-dot"></span>
      <span class="brand-name">Copperline Pipeworks, Inc.</span>
    </div>
    <div class="services">Residential<span class="sep">✱</span>Commercial<span class="sep">✱</span>Service</div>
  </section>
</body>
</html>
```